Flyer-Design für Artgerechte Tiernahrung
Zielgruppe
Napfstübchen. Artgerechte Tiernahrung.
Aufgabenstellung
DIN A5 Hochformat.
Fotos und Text in Drive unter https://ablage.wolkenfach-beispiel.de/ordner/7QK31xZmRtLw0YbVc8HnJe2PdUs5AgTf?freigabe=offen
Aus dem Flyer soll auch hervorgehen damit wir Geschirre etc. verkaufen. Gerne in einem der Bilder so das es auf den ersten Blick auch zu sehen ist.

```html
<!DOCTYPE html>
<html lang="de">
<head>
<meta charset="utf-8">
<title>Napfstübchen Tannwerder – Flyer</title>
<link rel="stylesheet" href="https://fonts.googleapis.com/css2?family=Amatic+SC:wght@700&family=Barlow:wght@400;600;700&display=swap">
<style>
  :root {
    --page-bg: #e6e6e6;
    --paper: #f3f3f3;
    --paper-shade: #e2e2e2;
    --sand: #b8aa8c;
    --sand-dark: #a89a7c;
    --brown: #4b3625;
    --text: #4f3e31;
    --text-soft: #efe8da;
    --rim: #f7f7f7;
  }
  * { box-sizing: border-box; margin: 0; padding: 0; }
  html, body { width: 1200px; height: 1200px; overflow: hidden; }
  body {
    background: var(--page-bg);
    font-family: "Barlow", sans-serif;
    color: var(--text);
  }
  .flyer {
    position: absolute;
    left: 211px; top: 50px;
    width: 778px; height: 1100px;
    overflow: hidden;
    background: linear-gradient(160deg, var(--paper) 0%, #fafafa 40%, var(--paper-shade) 100%);
    box-shadow: 0 10px 30px rgba(0,0,0,.15);
  }
  .flyer-shapes { position: absolute; inset: 0; width: 100%; height: 100%; }

  .photo {
    position: absolute;
    border-radius: 50%;
    border: 10px solid var(--rim);
    box-shadow: 0 6px 14px rgba(0,0,0,.18);
  }
  .photo--meat { left: 500px; top: -50px; width: 290px; height: 290px;
    background: radial-gradient(circle at 45% 45%, #8e2a35, #6d1d28 60%, #4e1520); }
  .photo--rice { left: -30px; top: 330px; width: 170px; height: 170px;
    background: radial-gradient(circle at 70% 45%, #6b1520 0 35%, #e9e3d6 55%, #d9d1c2); }
  .photo--fish { left: 70px; top: 470px; width: 250px; height: 250px;
    background: radial-gradient(circle at 65% 45%, #ef9a70, #f2c1a2 45%, #eadccf 75%); }
  .photo--veg { left: -50px; top: 730px; width: 155px; height: 155px;
    background: radial-gradient(circle at 60% 50%, #b8233e 0 25%, #d9c23a 45%, #5d9a3a 70%, #e8e8e8); }
  .photo--bowl { left: 380px; top: 650px; width: 540px; height: 540px;
    background: radial-gradient(circle at 55% 55%, #7b2c2c 0 35%, #9a4a3f 50%, #6d3b52 62%, #e77a38 72%, #ececec 82%); }

  .mascot {
    position: absolute; left: 370px; top: 70px;
    width: 110px; height: 185px;
    border-radius: 40px 40px 20px 20px;
    background: var(--sand-dark);
    opacity: .55;
  }

  .brand {
    position: absolute; left: 62px; top: 70px;
    font-family: "Amatic SC", cursive;
    font-weight: 700;
    line-height: .95;
  }
  .brand__line { display: block; }
  .brand__line--top { font-size: 64px; letter-spacing: 1px; color: var(--text-soft); }
  .brand__line--bottom { font-size: 84px; letter-spacing: 1px; color: var(--brown); }
  .tagline {
    position: absolute; left: 64px; top: 232px;
    font-size: 20px; line-height: 1.2;
    color: var(--text-soft);
  }

  .offer { position: absolute; left: 338px; top: 340px; width: 420px; }
  .offer__title { font-size: 20px; font-weight: 700; color: var(--brown); margin-bottom: 6px; }
  .offer__list { list-style: none; font-size: 18px; line-height: 1.45; }
  .offer__list li { position: relative; padding-left: 22px; }
  .offer__list li::before { content: "•"; position: absolute; left: 4px; }
  .offer__cta {
    margin-top: 26px; font-size: 19px; font-weight: 700;
    line-height: 1.3; color: var(--brown);
  }

  .contact { position: absolute; left: 92px; top: 815px; font-size: 17px; line-height: 1.5; font-style: normal; }
  .contact__name {
    font-family: "Amatic SC", cursive; font-weight: 700;
    font-size: 38px; color: var(--brown); margin-bottom: 14px; line-height: 1;
  }
  .contact__row { display: flex; align-items: center; gap: 10px; }
  .contact__row svg { width: 18px; height: 18px; }
  .contact__web { margin-bottom: 4px; }
</style>
</head>
<body>
  <main class="flyer">
    <svg class="flyer-shapes" viewBox="0 0 778 1100" preserveAspectRatio="none" aria-hidden="true">
      <defs>
        <linearGradient id="sand-bottom" x1="0" y1="0" x2="0" y2="1">
          <stop offset="0" stop-color="#d3cab8"/>
          <stop offset="1" stop-color="#e4dfd4"/>
        </linearGradient>
      </defs>
      <path d="M0 0 H778 V190 C700 195 620 215 545 240 C450 272 410 325 300 338 C190 350 90 305 0 322 Z" fill="var(--sand)"/>
      <path d="M0 705 C120 665 260 640 380 675 C470 702 540 712 620 690 L778 680 V1100 H0 Z" fill="url(#sand-bottom)"/>
    </svg>

    <div class="photo photo--meat" role="img" aria-label="Schüssel mit gewürfeltem rohem Rindfleisch"></div>
    <div class="photo photo--rice" role="img" aria-label="Schüssel mit Reis und Leberstücken"></div>
    <div class="photo photo--fish" role="img" aria-label="Schüssel mit Lachswürfeln und Garnelen"></div>
    <div class="photo photo--veg" role="img" aria-label="Schüssel mit Gemüsewürfeln"></div>
    <div class="photo photo--bowl" role="img" aria-label="Große Schüssel mit rohem Fleisch, Radicchio, Zucchini, Möhren und Orange"></div>

    <div class="mascot" role="img" aria-label="Linienzeichnung eines sitzenden Schäferhundes"></div>

    <h1 class="brand">
      <span class="brand__line brand__line--top">Napfstübchen</span>
      <span class="brand__line brand__line--bottom">Tannwerder</span>
    </h1>
    <p class="tagline">Ihr Rohwertig-Fachhändler für<br>artgerechte Tiernahrung</p>

    <section class="offer">
      <h2 class="offer__title">Das Beste für Ihre Vierbeiner:</h2>
      <ul class="offer__list">
        <li>BARF-Rohfutter, Ergänzungen und Öle</li>
        <li>Natürliche Kauartikel und Leckerlis</li>
        <li>Kräutermischungen für Hunde</li>
        <li>Equipment, Führ- und Zuggeschirre</li>
        <li>Laufgürtel und Leinen</li>
        <li>Kostenlose Futterberatung auch für<br>Nass- und Trockenfutter</li>
      </ul>
      <p class="offer__cta">Besuchen Sie uns vor Ort und<br>im Online-Shop und lassen Sie sich<br>professionell beraten.</p>
    </section>

    <address class="contact">
      <p class="contact__name">Napfstübchen Tannwerder</p>
      <p>Kiefernweg 12b</p>
      <p>17235 Seehausen OT Tannwerder</p>
      <p class="contact__web">www.kiefernpfoten.de</p>
      <p class="contact__row">
        <svg viewBox="0 0 20 20" fill="none" stroke="currentColor" stroke-width="1.4"><rect x="2" y="4" width="16" height="12" rx="1"/><path d="M2 5 L10 11 L18 5"/></svg>
        info@kiefernpfoten.de
      </p>
      <p class="contact__row">
        <svg viewBox="0 0 20 20" fill="none" stroke="currentColor" stroke-width="1.4"><path d="M5 2 L8 2 L9 6 L7 8 C8 11 9 12 12 13 L14 11 L18 12 L18 15 C18 17 16 18 14 18 C8 17 3 12 2 6 C2 4 3 2 5 2 Z"/></svg>
        0157 24 61 93 08
      </p>
    </address>
  </main>
</body>
</html>
```